Brush Cutting, Bush Hogging, Forestry Clearing, Dirt Work

We need a business card design design for a new company based in Summit, Ms. We specialize in under-brush clearing, forestry cutting, general bush hogging, heavy duty bush hogging, dirt work, gravel hauling, land clearing . We have bulldozers, compact track loaders, dump trucks, tractors. I will attach a picture of a compact track loader I would like to have on the card design if possible.

Industry/Entity Type

Business

Contact Information for Business Card

Harlan Field Mowers Summit, Ms. Wade Harlan Doug Swarts601-600-0373 601-555-0172

Font styles to use
Serif
Sans Serif

Requirements
Must have
• Must have a Kestrel compact track loader with a brush cutter as the attachment. not a dirt bucket.
Should not have
• should not have any other brand of machine but kestrel.

```html
<!DOCTYPE html>
<html lang="en">
<head>
<meta charset="utf-8">
<title>Harlan Field Mowers – Business Card</title>
<link rel="stylesheet" href="https://fonts.googleapis.com/css2?family=Crimson+Text:wght@400;600&display=swap">
<style>
  :root {
    --paper: #ffffff;
    --amber: #f0a23a;
    --amber-deep: #d98a25;
    --bark: #3a2e22;
    --bark-dark: #2a221b;
    --panel: #3b342e;
    --cream: #f3ead8;
    --ink-light: #f5f1ea;
  }
  * { margin: 0; padding: 0; box-sizing: border-box; }
  html, body {
    width: 694px; height: 1200px; overflow: hidden;
    background: var(--paper);
    font-family: "Crimson Text", Georgia, serif;
  }
  .canvas { position: relative; width: 694px; height: 1200px; }

  .card { position: absolute; left: 100px; width: 497px; height: 283px; overflow: hidden; }
  .card--front { top: 19px; }
  .card--back { top: 312px; background: var(--panel); }

  /* front */
  .machine-photo {
    position: absolute; left: 0; right: 0; top: 0; height: 211px;
    background:
      radial-gradient(ellipse at 40% 60%, #8a6a2a 0%, rgba(138,106,42,0) 40%),
      linear-gradient(160deg, #4a4a3c 0%, #2f2e26 45%, #5a564a 80%, #3c3a32 100%);
  }
  .front-band { position: absolute; left: 0; right: 0; top: 211px; bottom: 0; background: var(--bark); }
  .front-band__stripe { position: absolute; left: 0; right: 0; background: var(--amber); }
  .front-band__stripe--top { top: 0; height: 7px; }
  .front-band__stripe--main { top: 13px; height: 38px; background: linear-gradient(90deg, var(--amber-deep), var(--amber) 50%, var(--amber-deep)); }
  .front-band__stripe--bottom { top: 56px; height: 6px; }
  .front-band__title {
    position: absolute; left: 0; right: 0; top: 13px; height: 38px;
    display: flex; align-items: center; justify-content: center;
    font-size: 10px; letter-spacing: 4.6px; color: var(--bark); text-transform: uppercase;
  }

  /* back */
  .back-band { position: absolute; left: 0; right: 0; background: linear-gradient(90deg, var(--amber-deep), var(--amber) 50%, var(--amber-deep)); }
  .back-band--top { top: 0; height: 48px; }
  .back-band--bottom { bottom: 0; height: 40px; }
  .back-rule { position: absolute; left: 0; right: 0; }
  .back-rule--cream-top { top: 48px; height: 2px; background: var(--cream); }
  .back-rule--bark-top { top: 50px; height: 4px; background: var(--bark-dark); }
  .back-rule--bark-bottom { bottom: 45px; height: 4px; background: var(--bark-dark); }
  .back-rule--cream-bottom { bottom: 40px; height: 3px; background: var(--cream); }
  .faded-photo {
    position: absolute; left: 0; right: 0; top: 54px; bottom: 49px;
    background: linear-gradient(120deg, #4a4238 0%, #3b342e 45%, #4a3f2f 70%, #35302b 100%);
  }
  .back-title {
    position: absolute; left: 0; right: 0; top: 59px;
    text-align: center; font-size: 10px; letter-spacing: 4.6px;
    color: var(--ink-light); text-transform: uppercase;
  }
  .owners {
    position: absolute; left: 0; right: 0; top: 102px;
    text-align: center; font-size: 25px; font-weight: 400;
    color: var(--ink-light); word-spacing: 3px;
  }
  .phones { position: absolute; left: 188px; top: 145px; display: flex; gap: 8px; align-items: center; }
  .phones__icon { width: 14px; height: 35px; }
  .phones__list { list-style: none; font-size: 16px; line-height: 21px; color: var(--ink-light); }
</style>
</head>
<body>
<main class="canvas">
  <section class="card card--front">
    <div class="machine-photo" role="img" aria-label="Compact track loader with a brush cutter attachment clearing woodland"></div>
    <div class="front-band">
      <div class="front-band__stripe front-band__stripe--top"></div>
      <div class="front-band__stripe front-band__stripe--main"></div>
      <div class="front-band__stripe front-band__stripe--bottom"></div>
      <p class="front-band__title">Harlan Field Mowers Pellham Vale</p>
    </div>
  </section>

  <section class="card card--back">
    <div class="back-band back-band--top"></div>
    <div class="back-rule back-rule--cream-top"></div>
    <div class="back-rule back-rule--bark-top"></div>
    <div class="faded-photo" role="img" aria-label="Faded compact track loader behind the contact details"></div>
    <div class="back-rule back-rule--bark-bottom"></div>
    <div class="back-rule back-rule--cream-bottom"></div>
    <div class="back-band back-band--bottom"></div>

    <p class="back-title">Harlan Field Mowers Pellham Vale</p>
    <h1 class="owners">Wade Harlan&nbsp; Rory Penbeck</h1>
    <div class="phones">
      <svg class="phones__icon" viewBox="0 0 14 35" aria-hidden="true">
        <rect x="0" y="0" width="14" height="35" rx="2.5" fill="#ffffff"/>
        <rect x="2" y="3" width="10" height="26" fill="#f0a23a"/>
      </svg>
      <ul class="phones__list">
        <li>601-555-0148</li>
        <li>601-555-0172</li>
      </ul>
    </div>
  </section>
</main>
</body>
</html>
```